Australian IT Company New Logo Business Cards Required

We are a computer consultancy / MSP located in Brisbane Australia looking to have business cards designed with our new logo, we are looking for something professional that catches the eye.
I can provide the logo in other formats if required, let's see what you can create!

```html
<!DOCTYPE html>
<html lang="en">
<head>
<meta charset="utf-8">
<title>Norvale – Business Cards</title>
<link href="https://fonts.googleapis.com/css2?family=Montserrat:wght@500;700;800&family=Open+Sans:wght@400;600&display=swap" rel="stylesheet">
<style>
  :root {
    --bg: #0d0d0d;
    --card: #2b2c2e;
    --card-dark: #232426;
    --green: #7ed321;
    --text: #d9d9d9;
    --muted: #9a9b9d;
    --rule: #55575a;
  }
  * { box-sizing: border-box; margin: 0; padding: 0; }
  html, body { width: 1200px; height: 820px; overflow: hidden; background: var(--bg); }
  body {
    display: flex; align-items: center; justify-content: center; gap: 40px;
    font-family: "Open Sans", Arial, sans-serif;
  }
  .card {
    position: relative; width: 540px; height: 310px;
    background: linear-gradient(160deg, var(--card) 0%, var(--card-dark) 100%);
    overflow: hidden;
  }
  .card--front { border-left: 2px solid var(--green); border-bottom: 2px solid var(--green); }
  .card--back { box-shadow: 0 4px 0 var(--green), 0 7px 0 #4c8a12, 0 10px 0 var(--green); }

  .brand { position: absolute; display: flex; flex-direction: column; align-items: flex-start; }
  .brand__name {
    display: flex; align-items: center; gap: 10px;
    font-family: "Montserrat", Arial, sans-serif; font-weight: 800;
    color: var(--green); letter-spacing: 1px; line-height: 1;
  }
  .brand__dot { border-radius: 50%; background: var(--green); flex: none; }
  .brand__tagline {
    font-family: "Montserrat", Arial, sans-serif; font-weight: 500;
    color: var(--muted); text-transform: uppercase; letter-spacing: 2.4px;
  }
  .card--front .brand { left: 200px; top: 62px; }
  .card--front .brand__name { font-size: 44px; }
  .card--front .brand__dot { width: 22px; height: 22px; }
  .card--front .brand__tagline { font-size: 10.5px; margin: 8px 0 0 32px; }

  .divider { position: absolute; left: 205px; top: 166px; width: 300px; height: 1px; background: var(--rule); }

  .person { position: absolute; left: 36px; top: 156px; }
  .person__name {
    font-family: "Montserrat", Arial, sans-serif; font-weight: 700;
    font-size: 19px; color: var(--green); letter-spacing: .5px; text-transform: uppercase;
  }
  .person__role { font-size: 13px; color: var(--text); margin-top: 1px; }

  .contact { position: absolute; left: 40px; top: 214px; list-style: none; }
  .contact__item {
    display: flex; align-items: center; gap: 9px;
    font-size: 12.5px; color: var(--text); height: 19px;
  }
  .contact__item svg { width: 13px; height: 13px; flex: none; }
  .contact__accent { color: var(--green); }

  .address {
    position: absolute; right: 34px; top: 212px; text-align: right;
    font-size: 12.5px; line-height: 1.45; color: var(--text);
  }

  .arc-field {
    position: absolute; left: 0; bottom: 0; width: 330px; height: 260px;
    background: radial-gradient(circle at 0% 100%, #2a2b2d 0%, #3a3b3d 30%, #2c2d2f 45%, #3a3b3d 60%, #2c2d2f 75%, transparent 76%);
    opacity: .9;
  }
  .card--back .brand { right: 34px; top: 98px; align-items: flex-end; }
  .card--back .brand__name { font-size: 36px; }
  .card--back .brand__dot { width: 18px; height: 18px; }
  .card--back .brand__tagline { font-size: 9px; margin-top: 7px; }
</style>
</head>
<body>
  <section class="card card--front" aria-label="Business card front">
    <div class="brand">
      <div class="brand__name"><span class="brand__dot"></span>NORVALE</div>
      <div class="brand__tagline">IT Solutions for Small Business</div>
    </div>
    <div class="divider"></div>

    <div class="person">
      <div class="person__name">Marcus Hale</div>
      <div class="person__role">Managing Director</div>
    </div>

    <ul class="contact">
      <li class="contact__item">
        <svg viewBox="0 0 16 16" fill="none" stroke="var(--green)" stroke-width="1.8"><path d="M3 2.5l3 0 1 3.5-2 1.2a8 8 0 0 0 3.8 3.8L10 9l3.5 1v3c0 .6-.5 1-1 1A11 11 0 0 1 2 3.5c0-.5.4-1 1-1z"/></svg>
        044-555 010 234
      </li>
      <li class="contact__item">
        <svg viewBox="0 0 16 16" fill="none" stroke="var(--green)" stroke-width="1.8"><rect x="4" y="1.5" width="8" height="13" rx="1.5"/><line x1="7" y1="12" x2="9" y2="12"/></svg>
        044-555 010 235
      </li>
      <li class="contact__item">
        <svg viewBox="0 0 16 16" fill="var(--green)"><path d="M1 3h14v10H1z"/><path d="M1 3l7 6 7-6" fill="none" stroke="var(--card)" stroke-width="1.4"/></svg>
        info@norvale-it.com
      </li>
      <li class="contact__item">
        <svg viewBox="0 0 16 16" fill="none" stroke="var(--green)" stroke-width="1.4"><circle cx="8" cy="8" r="6.5"/><ellipse cx="8" cy="8" rx="3" ry="6.5"/><line x1="1.5" y1="8" x2="14.5" y2="8"/><line x1="2.5" y1="4.8" x2="13.5" y2="4.8"/><line x1="2.5" y1="11.2" x2="13.5" y2="11.2"/></svg>
        <span>www.<span class="contact__accent">norvale-it</span>.com</span>
      </li>
    </ul>

    <address class="address" style="font-style:normal">
      421, Address line goes here<br>45452, Country Name
    </address>
  </section>

  <section class="card card--back" aria-label="Business card back">
    <div class="arc-field" role="img" aria-label="Faint concentric arc decoration in dark grey tones"></div>
    <div class="brand">
      <div class="brand__name"><span class="brand__dot"></span>NORVALE</div>
      <div class="brand__tagline">IT Solutions for Small Business</div>
    </div>
  </section>
</body>
</html>
```